Luma Harbor Vow Studio, Inc.

Luma Harbor Vow Studio Business Card design for Cardlyne. Clean, contemporary, creative, colorful (using colors provided). ONE SIDE SHOULD INCLUDE logo, www.lumaharborvowstudio.com, @sayidoatluma. OTHER SIDE SHOULD INCLUDE Delia Brennan. Owner & Officiant. Coral Ridge, Marenta. 555.014.2871. delia@lumaharborvowstudio.com. Colors are blue #58AA9E
and golden #e2bf80)

Target Market(s)

Destination Wedding Clients in the United States

Contact Information for Business Card

Delia Brennan
Owner & Officiant
Coral Ridge, Marenta
555.014.2871
delia@lumaharborvowstudio.com

Font styles to use
Sans Serif

Requirements
Must have
• Colorful (colors are blue #58AA9E
• and golden #e2bf80), clean, contemporary. ONE SIDE SHOULD INCLUDE logo, www.lumaharborvowstudio.com, @sayidoatluma. Other side should include Delia Brennan. Owner & Officiant. Coral Ridge, Marenta. 555.014.2871. delia@lumaharborvowstudio.com
Nice to have
• I would like to see a version that includes my bio photo, and one that doesn't include the bio photo

```html
<!DOCTYPE html>
<html lang="en">
<head>
<meta charset="utf-8">
<title>Luma Harbor Vow Studio – Business Card</title>
<link rel="stylesheet" href="https://fonts.googleapis.com/css2?family=Roboto:wght@300;400&family=Roboto+Condensed:wght@500&display=swap">
<style>
  :root {
    --backdrop: #e7e2da;
    --card-white: #f7f7f6;
    --card-gold: #e2bf80;
    --sea-blue: #58aa9e;
    --gold-text: #d9b276;
    --ink: #4a4a4a;
    --shell-light: #d8eeea;
    --shell-mid: #a9d7cf;
  }
  * { margin: 0; padding: 0; box-sizing: border-box; }
  html, body { width: 1200px; height: 960px; overflow: hidden; }
  body { background: var(--backdrop); position: relative; font-family: "Roboto", Arial, sans-serif; }

  .card {
    position: absolute;
    width: 600px;
    height: 342px;
    border-radius: 22px;
    overflow: hidden;
    box-shadow: 0 3px 6px rgba(0,0,0,.25);
  }
  .card--front { left: 302px; top: 133px; background: var(--card-white); }
  .card--back  { left: 298px; top: 502px; height: 343px; background: var(--card-gold); }

  .person-name {
    position: absolute; left: 36px; top: 32px;
    font-family: "Roboto Condensed", "Arial Narrow", sans-serif;
    font-weight: 500; font-size: 25px; color: var(--sea-blue);
    letter-spacing: .2px;
  }
  .person-title {
    position: absolute; left: 36px; top: 60px;
    font-size: 14px; color: var(--gold-text); letter-spacing: .3px;
  }
  .contact-list { position: absolute; left: 34px; top: 89px; list-style: none; }
  .contact-list li {
    display: flex; align-items: center; height: 19px;
    font-size: 14px; color: var(--ink);
  }
  .contact-list li.small { font-size: 13px; }
  .contact-icon { width: 14px; height: 14px; margin-right: 10px; flex: none; }

  .shell-art { position: absolute; left: 0; top: 0; width: 600px; height: 342px; pointer-events: none; }

  .brand-mark {
    position: absolute; left: 50%; top: 96px; width: 44px; height: 44px;
    margin-left: -22px; border-radius: 50%; background: var(--shell-mid);
  }
  .brand-name {
    position: absolute; left: 0; right: 0; top: 188px; text-align: center;
    font-weight: 300; font-size: 36px; color: #ffffff; letter-spacing: .5px;
  }
</style>
</head>
<body>

<section class="card card--front" aria-label="Card front">
  <svg class="shell-art" viewBox="0 0 600 342" role="img" aria-label="Hand-drawn starfish, scallop shell with gold wedding rings and spiral seashell">
    <defs>
      <radialGradient id="shellGlow" cx="0.6" cy="0.55" r="0.6">
        <stop offset="0" stop-color="var(--shell-mid)"/>
        <stop offset="1" stop-color="var(--shell-light)"/>
      </radialGradient>
    </defs>
    <path d="M380 10 L460 40 L520 60 L560 150 L600 170 L600 320 L500 300 L440 330 L240 330 L220 230 L260 180 L330 170 L360 120 L330 80 Z" fill="url(#shellGlow)" opacity=".75"/>
  </svg>

  <h1 class="person-name">DELIA BRENNAN</h1>
  <p class="person-title">OWNER &amp; OFFICIANT</p>
  <ul class="contact-list">
    <li>
      <svg class="contact-icon" viewBox="0 0 14 14"><path d="M7 1a4 4 0 0 0-4 4c0 3 4 8 4 8s4-5 4-8a4 4 0 0 0-4-4zm0 5.5A1.5 1.5 0 1 1 7 3.5a1.5 1.5 0 0 1 0 3z" fill="var(--sea-blue)"/></svg>
      Coral Ridge, Marenta
    </li>
    <li>
      <svg class="contact-icon" viewBox="0 0 14 14"><path d="M3 1.5l2 .2 1 3-1.3 1.2a7 7 0 0 0 3.4 3.4L9.3 8l3 1 .2 2-1.5 1.5C6 12 2 8 1.5 3z" fill="var(--sea-blue)"/></svg>
      555.014.2871
    </li>
    <li class="small">
      <svg class="contact-icon" viewBox="0 0 14 14"><rect x="1" y="3" width="12" height="8" rx="1" fill="var(--sea-blue)"/><path d="M1.5 3.5L7 8l5.5-4.5" stroke="#fff" stroke-width="1.2" fill="none"/></svg>
      delia@lumaharborvowstudio.com
    </li>
    <li>
      <svg class="contact-icon" viewBox="0 0 14 14"><circle cx="7" cy="7" r="6" fill="var(--sea-blue)"/><path d="M1 7h12M7 1c-3 3-3 9 0 12M7 1c3 3 3 9 0 12" stroke="#fff" stroke-width="1" fill="none"/></svg>
      lumaharborvowstudio.com
    </li>
    <li>
      <svg class="contact-icon" viewBox="0 0 14 14"><circle cx="7" cy="7" r="5.5" fill="var(--sea-blue)"/></svg>
      @sayidoatluma
    </li>
  </ul>
</section>

<section class="card card--back" aria-label="Card back">
  <div class="brand-mark" aria-hidden="true"></div>
  <p class="brand-name">Luma Harbor Vow Studio</p>
</section>

</body>
</html>
```